Brindle Tavern & Lodge Supplies need a website

We need a website designed and created to facilitate us to promote & sell our products online. We buy excess / clearance lots of pub, cafe, restaurant & hotel furniture and equipment (usually from businesses that have excess inventory after a refurb or have closed down). We then sell these to other businesses mainly through our Chatterly page "Brindle Tavern & Lodge Supplies" but the process is cumbersome for the following reasons:
1) We dont have a stock list and images as it changes daily and people can only rely on recent posts and dont know if something is for sale still or is sold
2) we do not have the facility to sell online.

We are open to ideas and design concepts

We already have a logo & stationery deisgned

its probably best to look through our Chatterly page to better understand what we do

We would consider a catalogue / by department / category user interface such as:
https://brambleworth-trade-fittings.co.uk/

Our preference would be to change / delete / update stock via smartphone to best facilitate the maintenance of the website which i will do myself

Suggested categories would include:
Bar Furniture
Bar Equipment
Restaurant Furniture
Catering Equipment
Bedroom Furniture
Miscellaneous

Sub categories would include:
Bar Furniture:
Bar Stools
Bar Tables
Benches
Tub chairs
Arm chairs
Pub Mirrors
Pub Signs
Pub Memorabilia

Bar Equipment:
Bottle Coolers
Ice Machines
Glass Washers
Tills
Lighting
Sound
Wireless waiter
Glassware
Taps
Line coolers
Snooker tables
Pool tables
gaming machines

Restaurant Furniture:
Tables
Chairs
Wine racks
Dressers
Couches
Bench seating
Tub Chairs
Arm chairs
High chairs
Menu boards
Mirrors
Pictures

Catering Equipment:
Fridges
Freezers
Ovens
Cookers
Fryers
Carvery units
Hot display units
Refrigerated displays
Sinks
Stainless steel units
Microwaves
Mixers
Crockery
Cutlery
Utensils
Glassware

Bedroom Furniture:
Beds
Headboards
Wardrobes
Lockers
Dressing Tables
Mirrors
Lamps
Pictures

Profit sharing schemes:
Pool Tables
Juke Boxes
Gaming Machines

Target Market(s)

Pubs
Restaurants
cafes
guest houses
hotels

Industry/Entity Type

Hospitality

Number of Pages Required

5+ page

Colors

Designer to choose colors to be used in the design.

Requirements
Must have
• Website featuring our categories of stock to sell
Nice to have
• Ecommerce option
Should not have
• just a front page

```html
<!DOCTYPE html>
<html lang="en">
<head>
<meta charset="utf-8">
<title>Brindle Tavern & Lodge Supplies</title>
<link href="https://fonts.googleapis.com/css2?family=Signika:wght@400;600;700&display=swap" rel="stylesheet">
<style>
:root{
  --orange:#e68a00;
  --page:#ffffff;
  --band:#f7f7f7;
  --ink:#444444;
  --border:#cfcfcf;
  --navy-dark:#1b2a45;
  --navy-light:#3b5688;
  --link:#2f8fff;
  --footer:#272727;
  --footer-base:#1f1f1f;
  --footer-text:#dddddd;
  --brand-red:#a3161f;
  --icon:#c9c9c9;
}
*{margin:0;padding:0;box-sizing:border-box}
html,body{width:1200px;height:967px;overflow:hidden;background:var(--page)}
body{position:relative;font-family:"Signika",sans-serif;color:var(--ink)}
.abs{position:absolute}
.top-band{left:0;top:0;width:1200px;height:46px;background:var(--band)}
.btn-view{left:533px;top:10px;width:137px;height:29px;background:var(--orange);color:#fff;font-weight:600;font-size:14px;display:flex;align-items:center;justify-content:center;box-shadow:0 2px 3px rgba(0,0,0,.2)}
.partners-title{left:0;top:80px;width:1200px;text-align:center;font-size:19px;font-weight:600;letter-spacing:.5px;color:var(--ink)}
.carousel{left:161px;top:129px;width:896px;height:74px;border:1px solid var(--border);display:flex}
.carousel .cell{flex:1;border-right:1px solid var(--border);display:flex;align-items:center;justify-content:center}
.carousel .cell:last-child{border-right:none}
.partner-name{font-size:7.5px;font-weight:600;color:var(--brand-red);text-transform:uppercase;letter-spacing:.2px}
.arrow{top:152px}
.contact{left:0;top:244px;width:1200px;height:446px;background:radial-gradient(ellipse at 30% 70%,#34507f 0%,transparent 60%),linear-gradient(100deg,var(--navy-light) 0%,#2b416b 45%,var(--navy-dark) 100%)}
.contact-title{left:0;top:286px;width:1200px;text-align:center;color:#fff;font-size:30px;font-weight:600}
.field{left:224px;width:299px;height:37px;background:#fff;border:1px solid #ccc;font-size:11.5px;color:#777;padding:12px 7px 0}
.submit{left:225px;top:588px;width:298px;height:36px;background:var(--orange);color:#fff;font-size:17px;font-weight:600;display:flex;align-items:center;justify-content:center}
.c-head{color:#fff;font-size:14.5px;font-weight:600}
.c-text{color:#fff;font-size:11px;font-weight:600;line-height:16px}
.c-plain{color:#fff;font-size:11px;line-height:16px}
.c-link{color:var(--link);font-size:11.5px;font-weight:600;line-height:17px}
.badge{left:900px;top:508px;width:128px;height:26px;background:#f2f5f9;border:2px solid #cfe3f5;border-radius:3px}
.footer{left:0;top:690px;width:1200px;height:229px;background:var(--footer)}
.f-head{top:727px;color:#fff;font-size:14.5px;font-weight:600}
.f-list{top:755px;list-style:none;color:var(--footer-text);font-size:11.5px;font-weight:600;line-height:20.8px}
.social{left:876px;top:759px;display:flex;gap:12px;color:var(--footer-text);font-size:11.5px;font-weight:600}
.social span{display:flex;align-items:center;gap:5px}
.social i{display:block;width:10px;height:10px;background:var(--icon)}
.base{left:0;top:919px;width:1200px;height:48px;background:var(--footer-base);color:#fff;font-size:11.5px;font-weight:600;display:flex;align-items:center;justify-content:center}
</style>
</head>
<body>
<div class="abs top-band"></div>
<div class="abs btn-view">View All</div>

<h2 class="abs partners-title">Partners Websites</h2>
<svg class="abs arrow" style="left:70px" width="16" height="28" viewBox="0 0 16 28"><path d="M13 3 3 14l10 11" fill="none" stroke="#999" stroke-width="2"/></svg>
<div class="abs carousel">
  <div class="cell"><span class="partner-name">Brindle Tavern &amp; Lodge Supplies</span></div>
  <div class="cell"><span class="partner-name">Brindle Tavern &amp; Lodge Supplies</span></div>
  <div class="cell"><span class="partner-name">Brindle Tavern &amp; Lodge Supplies</span></div>
  <div class="cell"><span class="partner-name">Brindle Tavern &amp; Lodge Supplies</span></div>
  <div class="cell"><span class="partner-name">Brindle Tavern &amp; Lodge Supplies</span></div>
  <div class="cell"><span class="partner-name">Brindle Tavern &amp; Lodge Supplies</span></div>
</div>
<svg class="abs arrow" style="left:1116px" width="16" height="28" viewBox="0 0 16 28"><path d="M3 3l10 11L3 25" fill="none" stroke="#999" stroke-width="2"/></svg>

<section class="abs contact" role="img" aria-label="Blurred photo of a person typing on a laptop keyboard, in deep blue tones"></section>
<h2 class="abs contact-title">Contact Us</h2>

<div class="abs field" style="top:355px">Name</div>
<div class="abs field" style="top:400px">Email</div>
<div class="abs field" style="top:446px">Phone</div>
<div class="abs field" style="top:496px;height:83px">Message</div>
<div class="abs submit">SUBMIT</div>

<div class="abs c-head" style="left:613px;top:351px">Get in Touch</div>
<svg class="abs" style="left:613px;top:380px" width="18" height="26" viewBox="0 0 18 26"><path d="M9 1a8 8 0 0 0-8 8c0 6 8 16 8 16s8-10 8-16a8 8 0 0 0-8-8z" fill="#fff"/><circle cx="9" cy="9" r="3" fill="#2b416b"/></svg>
<div class="abs c-text" style="left:649px;top:377px">The Harrowgate Web Co<br>Ltd C/o 12, Kestrel Row<br>Upper Ashby Northshire<br>NR14 2QT</div>
<svg class="abs" style="left:617px;top:447px" width="12" height="19" viewBox="0 0 12 19"><rect x="1" y="1" width="10" height="17" rx="2" fill="none" stroke="#fff" stroke-width="1.6"/><circle cx="6" cy="15" r="1" fill="#fff"/></svg>
<div class="abs c-text" style="left:649px;top:448px">01632 960418</div>
<svg class="abs" style="left:613px;top:477px" width="19" height="14" viewBox="0 0 19 14"><rect x=".5" y=".5" width="18" height="13" fill="#fff"/><path d="M1 1l8.5 7L18 1M1 13l6-6M18 13l-6-6" fill="none" stroke="#2b416b" stroke-width="1.2"/></svg>
<div class="abs c-text" style="left:649px;top:475px">admin@harrowgate-web.co.uk</div>

<div class="abs c-head" style="left:613px;top:567px">Submit an advert</div>
<div class="abs c-link" style="left:613px;top:593px">Click here to use our online form<br>Click here for help with advertising</div>

<div class="abs c-head" style="left:900px;top:350px">Key Contact</div>
<div class="abs c-head" style="left:900px;top:374px;font-size:13px">Tom Ashcroft</div>
<div class="abs c-plain" style="left:900px;top:391px">Founder and owner of the<br>website and head of difficult<br>questions.</div>
<svg class="abs" style="left:903px;top:447px" width="12" height="19" viewBox="0 0 12 19"><rect x="1" y="1" width="10" height="17" rx="2" fill="none" stroke="#fff" stroke-width="1.6"/><circle cx="6" cy="15" r="1" fill="#fff"/></svg>
<div class="abs c-text" style="left:936px;top:448px">01632 960418</div>
<svg class="abs" style="left:900px;top:480px" width="19" height="14" viewBox="0 0 19 14"><rect x=".5" y=".5" width="18" height="13" fill="#fff"/><path d="M1 1l8.5 7L18 1M1 13l6-6M18 13l-6-6" fill="none" stroke="#2b416b" stroke-width="1.2"/></svg>
<div class="abs c-text" style="left:935px;top:478px">tom@fernlea.co.uk</div>
<div class="abs badge"></div>

<footer class="abs footer"></footer>
<div class="abs f-head" style="left:144px">Get to know us</div>
<ul class="abs f-list" style="left:144px"><li>Frequently asked quetions</li><li>Terms &amp; Conditions</li><li>Warning</li><li>Delivery</li><li>Banner Adervtising</li></ul>
<div class="abs f-head" style="left:378px">Categories</div>
<ul class="abs f-list" style="left:378px"><li>Bar Furniture</li><li>Bar Equipment</li><li>Restaurant Furniture</li><li>Catering Equipment</li><li>Bedroom Furniture</li><li>Miscellaneous</li></ul>
<div class="abs f-head" style="left:612px">Secondhand pub equipment</div>
<ul class="abs f-list" style="left:612px;top:756px"><li>About us</li><li>Careers</li><li>Partners websites</li><li>Shops</li></ul>
<div class="abs f-head" style="left:876px">Connect with us</div>
<div class="abs social"><span><i></i>Chatterly</span><span><i></i>Linkroll</span><span><i></i>Chirper</span></div>
<div class="abs base">© Harrowgate Web Co 2018 &nbsp;•</div>
</body>
</html>
```